Clear Strand Record Protocol Flyer

We need a flyer describing our initiative that seeks to develop and implement a standardized way of describing terrestrial fibre optic networks, which form the backbone of the Internet.
The primary audience that we are targeting is government and development decision makers and regulators, as well as businesses and groups involved in researching, planning, deploying and maintaining fibre optic infrastructure.

```html
<!DOCTYPE html>
<html lang="en">
<head>
<meta charset="utf-8">
<title>Clear Strand Record Protocol Flyer</title>
<link href="https://fonts.googleapis.com/css2?family=Montserrat:wght@500;600;700&family=Oswald:wght@500;600&family=Poppins:wght@400;500;600;700&display=swap" rel="stylesheet">
<style>
:root{
  --deep-blue:#1b18b4;
  --royal-blue:#3a2ee0;
  --night-purple:#1e0f63;
  --violet:#5530c9;
  --sky:#5ec6f6;
  --sky-soft:#86d4f8;
  --ink:#0b0b0d;
  --text:#1d1d22;
  --white:#ffffff;
  --paper:#ffffff;
  --stage:#f4f5f8;
}
*{margin:0;padding:0;box-sizing:border-box}
html,body{width:1200px;height:783px;overflow:hidden;background:var(--stage)}
body{position:relative;font-family:"Poppins",sans-serif;color:var(--text)}
.page{position:absolute;top:64px;width:509px;height:658px;background:var(--paper);overflow:hidden;box-shadow:0 6px 24px rgba(0,0,0,.12)}
.page--front{left:67px}
.page--back{left:635px}
.abs{position:absolute}
.photo{position:absolute;border-radius:50%;border:4px solid var(--sky)}
.heading{font-family:"Oswald",sans-serif;font-weight:600;font-size:18px;letter-spacing:.2px;color:var(--ink);line-height:1}
.heading span{color:var(--sky)}
.body-copy{font-size:8.2px;line-height:1.22;color:var(--text)}
.body-copy p+p{margin-top:9px}

/* front */
.hero{position:absolute;left:0;top:0;width:509px;height:342px;background:radial-gradient(ellipse at 30% 30%,var(--royal-blue),var(--deep-blue) 55%,#120f8f)}
.brand{left:30px;top:28px;font-family:"Montserrat",sans-serif;font-weight:500;font-size:58px;color:var(--white);letter-spacing:-1px;line-height:1}
.hero-photo{left:290px;top:4px;width:270px;height:270px;border:6px solid var(--white);background:linear-gradient(150deg,#c9ced6,#6e7c8f 55%,#2d3646)}
.title-1{left:29px;top:113px;font-family:"Montserrat",sans-serif;font-weight:500;font-size:43px;color:var(--white);line-height:1}
.title-2{left:28px;top:158px;font-family:"Oswald",sans-serif;font-weight:600;font-size:58px;color:var(--sky);line-height:1;letter-spacing:-.5px}
.title-3{left:29px;top:222px;font-family:"Montserrat",sans-serif;font-weight:500;font-size:24px;color:var(--white);line-height:1}
.title-3 b{font-weight:700}
.tagline{left:29px;top:253px;font-family:"Montserrat",sans-serif;font-size:16.5px;color:var(--white);line-height:1.22}
.callout{left:53px;top:304px;width:403px;height:76px;background:var(--white);border-radius:6px;box-shadow:0 4px 12px rgba(0,0,0,.18);padding:9px 20px;text-align:center;font-size:7.6px;font-weight:600;color:var(--ink);line-height:1.3}
.callout p+p{margin-top:8px}
.front-problem{left:29px;top:401px}
.rule{left:186px;top:409px;width:270px;height:1px;background:var(--sky-soft)}
.front-col-a{left:29px;top:428px;width:210px}
.front-col-b{left:265px;top:428px;width:205px}
.cta{font-size:8.8px;font-weight:700;color:var(--ink);line-height:1.35;text-transform:uppercase}
.front-cta{left:30px;top:546px;width:220px}
.front-photo-a{left:251px;top:508px;width:112px;height:112px;background:linear-gradient(135deg,#d79b2e,#4b3a2a 60%,#1c2230)}
.front-photo-b{left:363px;top:508px;width:112px;height:112px;background:linear-gradient(135deg,#4a6b8a,#1d2836 60%,#0d1117)}
.footer-band{left:0;bottom:0;width:509px;height:64px}
.contact{display:flex;align-items:center;gap:6px;font-size:11.5px;color:var(--white);font-family:"Montserrat",sans-serif;font-weight:500}
.contact .dot{width:11px;height:11px;border-radius:50%;background:var(--sky)}
.contact .sq{width:9px;height:9px;border-radius:50%;background:#2a66d9}
.front-contact{left:29px;top:608px;gap:16px;display:flex}

/* back */
.band{left:0;top:0;width:509px;height:144px;background:linear-gradient(110deg,var(--night-purple),#2a1690 45%,var(--violet))}
.band .heading{color:var(--white)}
.back-solve{left:29px;top:30px;font-size:19px}
.solve-col{top:55px;font-size:8.2px;line-height:1.22;color:var(--white)}
.solve-a{left:29px;width:170px}
.solve-b{left:205px;width:140px}
.solve-c{left:352px;width:140px}
.back-problem{left:29px;top:174px;font-size:19px}
.points{left:29px;top:201px;width:210px;list-style:none}
.points li{position:relative;padding-left:11px;font-size:8.2px;line-height:1.22;margin-bottom:9px}
.points li::before{content:"";position:absolute;left:0;top:2px;width:6px;height:6px;border-radius:50%;background:var(--sky)}
.points b{color:#3aa9e6;font-weight:600}
.data-label{width:120px;text-align:center;font-size:8.2px;font-weight:600;line-height:1.2;color:var(--ink);text-transform:uppercase}
.data-label .big{display:block;font-family:"Montserrat",sans-serif;font-weight:700;font-size:15px;color:var(--sky);line-height:1.05}
.label-a{left:248px;top:172px}
.label-b{left:365px;top:172px}
.label-b .big{margin-top:1px}
.tablet{top:228px;width:85px;height:112px;border:4px solid #111;border-radius:5px;background:#fff;box-shadow:0 8px 10px rgba(0,0,0,.15)}
.tablet-a{left:266px}
.tablet-b{left:381px}
.screen-code{position:absolute;inset:3px;background:linear-gradient(180deg,#f5f7fa,#e8edf3)}
.screen-map{position:absolute;inset:3px;background:linear-gradient(135deg,#b7d7a6,#e8e2cf 55%,#cfe0ee)}
.pen{top:270px;width:3px;height:70px;background:#222;border-radius:2px}
.back-photo{width:96px;height:96px}
.bp-1{left:39px;top:366px;background:linear-gradient(135deg,#c86a2e,#3b2a25)}
.bp-2{left:127px;top:366px;background:linear-gradient(135deg,#9aa8b4,#46382f)}
.bp-3{left:39px;top:478px;background:linear-gradient(135deg,#e8edf2,#7a8ea4)}
.bp-4{left:127px;top:478px;background:linear-gradient(135deg,#7fb8a8,#23443f)}
.who{left:266px;top:414px;font-size:19px}
.who-copy{left:266px;top:439px;width:215px}
.back-cta{left:29px;top:600px;width:240px;color:var(--white)}
.back-contact{left:265px;top:608px;gap:16px;display:flex}
.back-contact .contact{color:var(--ink)}
</style>
</head>
<body>

<!-- Front page -->
<section class="page page--front">
  <div class="hero"></div>
  <div class="abs brand">csrp</div>
  <div class="photo hero-photo" role="img" aria-label="Photo of a businessman in a suit using a smartphone"></div>
  <div class="abs title-1">Connecting</div>
  <div class="abs title-2">THE WORLD</div>
  <div class="abs title-3">with <b>Open Standards</b></div>
  <div class="abs tagline">Affordable, reliable Internet starts<br>with shared data and collaboration</div>
  <div class="abs callout">
    <p>Everyone deserves access to affordable and reliable Internet, no matter their location or circumstance.</p>
    <p>Meeting this challenge requires a community working together, ideally using shared standards and data to ensure the networks they plan and build interconnect with the global Internet.</p>
  </div>

  <h2 class="abs heading front-problem">WHAT’S <span>THE PROBLEM?</span></h2>
  <div class="abs rule"></div>
  <div class="abs body-copy front-col-a">
    <p>Fibre optic infrastructure forms the backbone of the Internet, underpinning all Internet access technologies, including mobile, wireless, and satellite.</p>
    <p>Despite its importance, the telecom sector and relevant government agencies often lack consistent and readily available data to help them plan, maintain, expand, and protect it.</p>
  </div>
  <div class="abs body-copy front-col-b">
    <p>This can cause multiple problems, including unknowingly duplicating existing infrastructure, not identifying gaps or single points of failure in current infrastructure, and not being able to effectively measure the socioeconomic impact of investments in Internet infrastructure.</p>
  </div>

  <p class="abs cta front-cta">Join our community to inform policy and investment decisions that can make the Internet for everyone.</p>

  <svg class="abs footer-band" viewBox="0 0 509 64" aria-hidden="true">
    <rect width="509" height="64" fill="var(--sky-soft)"/>
    <path d="M0 0 H330 C300 0 300 48 260 48 H0 Z" fill="var(--ink)"/>
  </svg>
  <div class="photo front-photo-a" role="img" aria-label="Photo of a technician working on fibre cabling in a network cabinet"></div>
  <div class="photo front-photo-b" role="img" aria-label="Photo of two professionals reviewing data in a server room"></div>
  <div class="abs front-contact">
    <span class="contact"><span class="dot"></span>www.csrp-network.org</span>
    <span class="contact">@Connect <span class="sq"></span></span>
  </div>
</section>

<!-- Back page -->
<section class="page page--back">
  <div class="abs band"></div>
  <h2 class="abs heading back-solve">HOW DOES <span>CSRP</span> SOLVE THIS?</h2>
  <p class="abs solve-col solve-a">The Clear Strand Record Protocol (CSRP) is common language for describing terrestrial fibre optic networks. It also works to establish norms among operators and regulators for information sharing regarding terrestrial fibre deployments.</p>
  <p class="abs solve-col solve-b">The standard facilitates the exchange, analysis, and visualization of fibre network data for different stakeholders, including governments, telecom providers, and researchers.</p>
  <p class="abs solve-col solve-c">By providing a consistent schema, CSRP enhances interoperability, transparency, and informed decision-making in broadband expansion and resilience efforts</p>

  <h2 class="abs heading back-problem">WHAT’S <span>THE PROBLEM?</span></h2>
  <ul class="abs points">
    <li><b>Governments and communication regulators</b> can assess national network infrastructure holistically to identify gaps in infrastructure and areas of network fragility. CSRP also helps avoid duplication in reporting of fibre infrastructure where multiple operators may report fibre on a single deployment.</li>
    <li><b>Investors and planners</b> can make more informed data-driven decisions on infrastructure development.</li>
    <li><b>Surveyors, engineers, and researchers</b> can access standardized data through GIS tools and mapping platforms.</li>
  </ul>

  <div class="abs data-label label-a"><span class="big">CSRP DATA</span>Describing Brazil’s<br>fibre network</div>
  <div class="abs data-label label-b">Visualization of<span class="big">CSRP DATA</span></div>
  <div class="abs tablet tablet-a"><div class="screen-code" role="img" aria-label="Tablet screen showing structured network data records"></div></div>
  <div class="abs pen" style="left:356px"></div>
  <div class="abs tablet tablet-b"><div class="screen-map" role="img" aria-label="Tablet screen showing a map of fibre routes and nodes"></div></div>
  <div class="abs pen" style="left:471px"></div>

  <div class="photo back-photo bp-1" role="img" aria-label="Photo of a team collaborating around a table"></div>
  <div class="photo back-photo bp-2" role="img" aria-label="Photo of two colleagues reviewing a document"></div>
  <div class="photo back-photo bp-3" role="img" aria-label="Photo of a person analysing data on a computer"></div>
  <div class="photo back-photo bp-4" role="img" aria-label="Photo of hands working with digital network overlays"></div>

  <h2 class="abs heading who">WHO’S <span>INVOLVED?</span></h2>
  <div class="abs body-copy who-copy">
    <p>Established in 2022, the CSRP has been developed in collaboration with the Global Development Fund, International Network Council, the Open Web Alliance, Ember Browser Group, Riverline Telecom, Quadrant Fibre, and Digital Forum Africa.</p>
    <p>The Open Web Alliance assumed a secretariat role for the standard in 2025 and is working to advance awareness and adoption of it worldwide through in-person workshops and technical assistance.</p>
  </div>

  <svg class="abs footer-band" viewBox="0 0 509 64" aria-hidden="true">
    <rect width="509" height="64" fill="var(--sky-soft)"/>
    <path d="M0 0 H270 C250 0 250 48 215 48 H0 Z" fill="var(--ink)"/>
  </svg>
  <p class="abs cta back-cta">Join our community to inform policy and investment decisions that can make the Internet for everyone.</p>
  <div class="abs back-contact">
    <span class="contact"><span class="dot"></span>www.csrp-network.org</span>
    <span class="contact">@Connect <span class="sq"></span></span>
  </div>
</section>

</body>
</html>
```